St Louis Electrician Needing a Business Card Design!!

We are a St Louis based electrical contracting firm that needs help designing a business card. We have a logo and I have another image that I would like to incorporate. Open to ideas..Thanks!!

Industry/Entity Type

Business

Requirements
Must have
• there are two downloads...one is the logo and the other is what i was wanting coming off the logo...the light rays. Like the logo with the blue background...Was thinking the whole card would be that color blue.
Should not have
• No lightning bolts

```html
<!DOCTYPE html>
<html lang="en">
<head>
<meta charset="utf-8">
<title>Brightline Power Co. – Business Card</title>
<link rel="stylesheet" href="https://fonts.googleapis.com/css2?family=Tinos&display=swap">
<style>
  :root {
    --card-blue: #0a55a8;
    --card-blue-deep: #062f6a;
    --card-blue-light: #1d6fc6;
    --glow-white: #ffffff;
    --ray-bright: rgba(235, 245, 255, 0.85);
    --ray-mid: rgba(200, 225, 255, 0.45);
    --ray-fade: rgba(150, 200, 255, 0);
  }
  * { margin: 0; padding: 0; box-sizing: border-box; }
  html, body {
    width: 1200px;
    height: 686px;
    overflow: hidden;
    background: var(--card-blue-deep);
  }
  .business-card {
    position: relative;
    width: 1200px;
    height: 686px;
    overflow: hidden;
    background:
      radial-gradient(ellipse 420px 260px at 20% 20%, var(--card-blue-light) 0%, transparent 70%),
      radial-gradient(ellipse 380px 240px at 85% 75%, var(--card-blue-light) 0%, transparent 70%),
      radial-gradient(ellipse 360px 220px at 15% 85%, var(--card-blue-deep) 0%, transparent 75%),
      radial-gradient(ellipse 340px 200px at 80% 15%, var(--card-blue-deep) 0%, transparent 75%),
      var(--card-blue);
    font-family: "Tinos", "Times New Roman", serif;
    color: var(--glow-white);
  }
  .light-burst {
    position: absolute;
    left: 0;
    top: 0;
    width: 1200px;
    height: 686px;
    background:
      radial-gradient(ellipse 90px 90px at 634px 372px, var(--ray-bright) 0%, var(--ray-fade) 100%),
      radial-gradient(ellipse 560px 60px at 600px 355px, var(--ray-bright) 0%, var(--ray-fade) 100%),
      radial-gradient(ellipse 600px 130px at 610px 360px, var(--ray-mid) 0%, var(--ray-fade) 100%),
      radial-gradient(ellipse 220px 200px at 634px 372px, var(--ray-mid) 0%, var(--ray-fade) 100%),
      radial-gradient(ellipse 300px 240px at 960px 300px, rgba(200,225,255,0.25) 0%, var(--ray-fade) 100%);
  }
  .brand-name {
    position: absolute;
    left: 150px;
    top: 290px;
    width: 780px;
    text-align: center;
    font-size: 92px;
    line-height: 1;
    font-weight: 400;
    color: var(--glow-white);
    letter-spacing: 1px;
    white-space: nowrap;
  }
  .contact-line {
    position: absolute;
    left: 0;
    width: 1200px;
    top: 568px;
    text-align: center;
    font-size: 46px;
    line-height: 1;
    color: var(--glow-white);
    white-space: nowrap;
    text-shadow: 0 2px 6px rgba(0, 20, 60, 0.6);
  }
  .contact-line .separator { margin: 0 8px; }
</style>
</head>
<body>
  <main class="business-card">
    <div class="light-burst" role="img" aria-label="Radiating white light rays bursting out from behind the company name"></div>

    <p class="brand-name">Brightline Power Co.</p>

    <p class="contact-line">
      <span class="contact-name">Dana Whitfield</span><span class="separator">•</span><span class="contact-title">Account Rep</span><span class="separator">•</span><span class="contact-phone">555.012.4477</span>
    </p>
  </main>
</body>
</html>
```